Yukisaro Sports Company Business Card and Logo Design

We need a business card design for a new company based in Tokyo. Our company is the first e-commerce business to sell Japanese baseball apparel to the English speaking market. We have 3 of the 12 Japanese teams on board with us at the moment. Although we will be starting with baseball we will venture into other sports as well. The name of the company is "yukisaro" sports. Yukisaro means - a bridge connecting two sides with differences, such as people, countries, and cultures. We would like our bridge to promote apparel. I would like a slick,modern design(business card) that screams "wow" the minute one sees it.

Industry/Entity Type

Business

Contact Information for Business Card

Nagisaro RW Bldg. 4F
3-8-22 Nagisaro, Minato-ku
Tokyo, Japan 108-0097

Font styles to use
Serif

```html
<!DOCTYPE html>
<html lang="en">
<head>
<meta charset="utf-8">
<title>Yukisaro Sports Company – Business Card</title>
<link rel="stylesheet" href="https://fonts.googleapis.com/css2?family=Open+Sans:wght@400;600;700&display=swap">
<style>
  :root {
    --bg-top: #5a5b60;
    --bg-bottom: #2f3034;
    --card-white: #ffffff;
    --navy: #14205a;
    --navy-deep: #0c1640;
    --ink: #1c2a66;
    --cyan: #1fa3dc;
    --grey-text: #6b6f7a;
  }
  * { box-sizing: border-box; margin: 0; padding: 0; }
  html, body { width: 900px; height: 1200px; overflow: hidden; }
  body {
    background: linear-gradient(180deg, var(--bg-top), var(--bg-bottom));
    font-family: "Open Sans", Arial, sans-serif;
    position: relative;
  }
  .card {
    position: absolute;
    left: 90px;
    width: 720px;
    height: 411px;
    border-radius: 6px;
    overflow: hidden;
    box-shadow: 0 18px 40px rgba(0,0,0,0.45);
  }
  .card--front { top: 150px; background: var(--card-white); }
  .card--back {
    top: 640px;
    background: radial-gradient(ellipse at 50% 45%, var(--navy), var(--navy-deep));
    display: flex; align-items: center; justify-content: center;
  }
  .person { position: absolute; left: 60px; top: 64px; }
  .person__name { font-size: 30px; font-weight: 700; color: var(--ink); letter-spacing: -0.3px; white-space: nowrap; }
  .person__title { font-size: 17px; font-weight: 600; color: var(--cyan); margin-top: 2px; }
  .contact { position: absolute; left: 330px; top: 160px; list-style: none; }
  .contact__item {
    display: flex; align-items: flex-start; gap: 14px;
    font-size: 15px; color: var(--grey-text); line-height: 1.45; margin-bottom: 12px;
  }
  .contact__icon { width: 18px; height: 18px; flex: none; margin-top: 2px; }
  .contact__icon * { fill: var(--cyan); }
  .brand-disc {
    position: absolute; left: -70px; bottom: -90px;
    width: 260px; height: 260px; border-radius: 50%;
    background: var(--cyan); opacity: 0.9;
  }
  .brand { display: flex; align-items: center; gap: 20px; }
  .brand__mark { width: 44px; height: 44px; border-radius: 50%; background: var(--cyan); flex: none; }
  .brand__name { font-size: 46px; font-weight: 600; color: #ffffff; letter-spacing: 0.5px; white-space: nowrap; }
</style>
</head>
<body>
  <section class="card card--front" aria-label="Business card front">
    <div class="brand-disc" aria-hidden="true"></div>
    <div class="person">
      <p class="person__name">Thomas Brightwell</p>
      <p class="person__title">Sales Manager</p>
    </div>
    <ul class="contact">
      <li class="contact__item">
        <svg class="contact__icon" viewBox="0 0 24 24"><path d="M6.6 10.8a15 15 0 0 0 6.6 6.6l2.2-2.2c.3-.3.7-.4 1-.2 1.1.4 2.3.6 3.6.6.6 0 1 .4 1 1V20c0 .6-.4 1-1 1A17 17 0 0 1 3 4c0-.6.4-1 1-1h3.5c.6 0 1 .4 1 1 0 1.3.2 2.5.6 3.6.1.3 0 .7-.2 1z"/></svg>
        <span>+81 3 5412 7780</span>
      </li>
      <li class="contact__item">
        <svg class="contact__icon" viewBox="0 0 24 24"><rect x="6" y="2" width="12" height="20" rx="2"/></svg>
        <span>+81 90 2245 6613</span>
      </li>
      <li class="contact__item">
        <svg class="contact__icon" viewBox="0 0 24 24"><path d="M2 5h20v14H2z M2 5l10 8 10-8"/></svg>
        <span>info@yukisaro.jp</span>
      </li>
      <li class="contact__item">
        <svg class="contact__icon" viewBox="0 0 24 24"><path d="M12 2a7 7 0 0 0-7 7c0 5 7 13 7 13s7-8 7-13a7 7 0 0 0-7-7zm0 9.5a2.5 2.5 0 1 1 0-5 2.5 2.5 0 0 1 0 5z"/></svg>
        <span>Nagisaro RW Bldg. 4F<br>3-8-22 Nagisaro, Minato-ku<br>Tokyo, Japan 108-0097</span>
      </li>
    </ul>
  </section>

  <section class="card card--back" aria-label="Business card back">
    <div class="brand">
      <span class="brand__mark" aria-hidden="true"></span>
      <span class="brand__name">yukisaro sports</span>
    </div>
  </section>
</body>
</html>
```